Cedarline Joinery eye catching business card

I need an eye catching business card that reflects my traditional, fun, handmade woodcraft shop. I make high end custom furniture and fine woodworking products, a lot of which are rustic, natural looking. We are a small shop but we produce awesome, one of a kind wood products, and our business card should reflect that. Our target audience is young professionals to retired folks who want a quality, local, handmade product. I'd like the Shop Nearby logo somewhere on the card, BUT not overwhelming, the main focus is my Logo, no preference on color whichever looks the best. Visit my website to get a feel for my company. Cedarlinejoinery.com
Target Market(s)
young professionals to retired folks. Any one who wants to furnish their home with quality handcrafted products.
Industry/Entity Type
Business
Contact Information for Business Card
Marlo Finch (555)417-6382
marlo@cedarlinejoinery.com
www.cedarlinejoinery.com
Look and feel

```html
<!DOCTYPE html>
<html lang="en">
<head>
<meta charset="utf-8">
<title>Cedarline Joinery — Business Card</title>
<link rel="stylesheet" href="https://fonts.googleapis.com/css2?family=Cinzel:wght@400&family=Montserrat:wght@400;600&display=swap">
<style>
  :root {
    --page: #efedf0;
    --card: #ffffff;
    --olive: #8c8652;
    --wood-light: #9a8866;
    --wood-mid: #6f6248;
    --wood-dark: #4f4534;
    --logo-text: #ffffff;
    --shadow: rgba(40, 30, 45, 0.18);
  }
  * { margin: 0; padding: 0; box-sizing: border-box; }
  html, body {
    width: 1200px;
    height: 1000px;
    overflow: hidden;
    background: var(--page);
  }
  .sheet {
    width: 1200px;
    height: 1000px;
    display: flex;
    flex-direction: column;
    align-items: center;
    justify-content: center;
    gap: 60px;
  }
  .card {
    width: 700px;
    height: 400px;
    background: var(--card);
    box-shadow: 0 8px 24px var(--shadow);
    position: relative;
  }
  .card--front {
    display: flex;
    align-items: center;
    justify-content: center;
  }
  .wood-panel {
    width: 440px;
    height: 150px;
    background: linear-gradient(100deg, var(--wood-mid) 0%, var(--wood-light) 35%, var(--wood-mid) 60%, var(--wood-light) 85%, var(--wood-dark) 100%);
    display: flex;
    align-items: center;
    justify-content: center;
  }
  .logo-name {
    font-family: "Montserrat", sans-serif;
    font-weight: 600;
    font-size: 34px;
    letter-spacing: 4px;
    color: var(--logo-text);
    text-transform: uppercase;
  }
  .card--back {
    display: flex;
    flex-direction: column;
    align-items: center;
    justify-content: center;
    color: var(--olive);
    text-align: center;
  }
  .business-name {
    font-family: "Cinzel", serif;
    font-weight: 400;
    font-size: 40px;
    letter-spacing: 2px;
    text-transform: uppercase;
    margin-bottom: 28px;
  }
  .website,
  .contact-line {
    font-family: "Montserrat", sans-serif;
    font-weight: 400;
    font-size: 13px;
    letter-spacing: 1.5px;
    text-transform: uppercase;
  }
  .website { margin-bottom: 40px; }
</style>
</head>
<body>
  <main class="sheet">
    <section class="card card--front" aria-label="Business card front">
      <div class="wood-panel" role="img" aria-label="Weathered reclaimed wood plank texture behind the shop name">
        <span class="logo-name">Cedarline Joinery</span>
      </div>
    </section>

    <section class="card card--back" aria-label="Business card back">
      <h1 class="business-name">Cedarline Joinery</h1>
      <p class="website">www.cedarlinejoinery.com</p>
      <p class="contact-line">Marlo Finch | marlo@cedarlinejoinery.com | (555)417-6382</p>
    </section>
  </main>
</body>
</html>
```